Kestrelmoor Advisory Services LLC
The Quiet Hand Consutants
Project: Kestrelmoor Advisory Services LLC
Kestrelmoor Advisory Services LLC - Financial Services
Creative Brief
Professional
Warrick Dunstan Hollowell
Senior Managing Director
388 West 19th Street New York, N.T. 10024
whollowell@kmaservices.net
KESTRELMOORADVISORYSERVICES.COM

```html
<!DOCTYPE html>
<html lang="en">
<head>
<meta charset="utf-8">
<title>Kestrelmoor Advisory Services LLC – Stationery</title>
<link href="https://fonts.googleapis.com/css2?family=Cinzel:wght@400;600&family=Lato:wght@400;700&display=swap" rel="stylesheet">
<style>
:root{
  --navy:#1d2f5c;
  --blue:#1f7fd0;
  --blue-dark:#0d4f9e;
  --gold:#c9a04a;
  --paper:#ffffff;
  --edge:#d9dde3;
  --grey:#6b7280;
  --bg:#ffffff;
}
*{margin:0;padding:0;box-sizing:border-box}
html,body{width:1200px;height:310px;overflow:hidden;background:var(--bg)}
.canvas{position:relative;width:1200px;height:310px;font-family:"Lato",sans-serif;color:var(--navy);overflow:hidden}
.piece{position:absolute;background:var(--paper);box-shadow:0 1px 4px rgba(0,0,0,.18);overflow:hidden}
.name{font-family:"Cinzel",serif;font-weight:600;color:var(--navy);line-height:1.1;text-align:center}
.small{font-size:4.5px;color:var(--grey);line-height:1.45}

.brand{position:absolute;left:20px;top:14px;width:210px;text-align:center}
.brand .dot{display:block;width:40px;height:40px;border-radius:50%;background:var(--blue);margin:0 auto 10px}
.brand .name{font-size:14px;letter-spacing:.3px}
.brand .name .line-two{font-size:18px}
.brand .tagline{font-family:"Cinzel",serif;font-size:7px;color:var(--navy);margin-top:6px}

.card-front{left:10px;top:178px;width:118px;height:50px}
.card-front .name{position:absolute;left:7px;top:16px;font-size:5px;text-align:left;width:38px}
.card-front .details{position:absolute;left:50px;top:6px;width:64px}
.card-front .person{font-weight:700;color:var(--navy)}
.card-blank{left:10px;top:246px;width:124px;height:50px}
.card-blank .name{position:absolute;left:7px;top:10px;font-size:5px;text-align:left}
.card-blank .web{position:absolute;bottom:5px;left:7px;font-size:3.8px;color:var(--grey);white-space:nowrap}
.card-blue{left:139px;top:246px;width:124px;height:50px;background:radial-gradient(circle at 55% 45%,var(--blue),var(--blue-dark));display:flex;align-items:center;justify-content:center}
.card-blue .name{color:#fff;font-size:6px}

.letterhead{top:19px;width:134px;height:281px}
.letterhead .name{position:absolute;font-size:5px;width:70px;top:14px}
.letterhead .footer{position:absolute;bottom:8px;left:0;right:0;text-align:center;font-size:3.6px;color:var(--grey);white-space:nowrap}
.lh-one{left:269px}
.lh-one .name{left:32px}
.lh-two{left:418px}
.lh-two .name{left:10px;text-align:left}
.lh-two .details{position:absolute;left:78px;top:12px;width:50px}

.slip{left:696px;width:134px;height:100px}
.slip .name{position:absolute;left:10px;top:10px;font-size:5px;width:64px;text-align:left}
.slip .details{position:absolute;left:10px;top:34px;width:70px}
.slip-one{top:30px}
.slip-two{top:180px}

.envelope{position:absolute;left:936px;width:248px;height:78px;background:var(--paper);box-shadow:0 1px 4px rgba(0,0,0,.2);overflow:hidden}
.envelope svg{position:absolute;left:0;top:0}
.envelope .name{position:absolute;font-size:5px;width:80px;left:84px;top:16px}
.env-gold{top:52px}
.env-blue{top:136px}
.env-white{top:220px}
.env-blue .name,.env-gold .name{color:#fff}
</style>
</head>
<body>
<div class="canvas">

  <header class="brand">
    <span class="dot"></span>
    <div class="name">KESTRELMOOR ADVISORY<br><span class="line-two">SERVICES</span></div>
    <div class="tagline">The Quiet Hand Consutants</div>
  </header>

  <section class="piece card-front">
    <div class="name">Kestrelmoor</div>
    <div class="details small">
      <div class="person">Warrick Dunstan Hollowell</div>
      <div>Senior Managing Director</div>
      <div>388 West 19th Street<br>New York, N.T. 10024</div>
      <div>whollowell@kmaservices.net</div>
    </div>
  </section>

  <section class="piece card-blank">
    <div class="name">Kestrelmoor</div>
    <div class="web">KESTRELMOORADVISORYSERVICES.COM</div>
  </section>

  <section class="piece card-blue">
    <div class="name">Kestrelmoor</div>
  </section>

  <section class="piece letterhead lh-one">
    <div class="name">Kestrelmoor Advisory Services LLC</div>
    <div class="footer">KESTRELMOORADVISORYSERVICES.COM</div>
  </section>

  <section class="piece letterhead lh-two">
    <div class="name">Kestrelmoor Advisory Services LLC</div>
    <div class="details small">
      <div>388 West 19th Street<br>New York, N.T. 10024</div>
      <div>whollowell@kmaservices.net</div>
    </div>
    <div class="footer">KESTRELMOORADVISORYSERVICES.COM</div>
  </section>

  <section class="piece slip slip-one">
    <div class="name">Kestrelmoor Advisory Services LLC</div>
    <div class="details small">388 West 19th Street<br>New York, N.T. 10024</div>
  </section>

  <section class="piece slip slip-two">
    <div class="name">Kestrelmoor Advisory Services LLC</div>
    <div class="details small">388 West 19th Street<br>New York, N.T. 10024</div>
  </section>

  <section class="envelope env-gold">
    <svg width="248" height="78" viewBox="0 0 248 78" aria-hidden="true">
      <defs><linearGradient id="goldFlap" x1="0" y1="0" x2="0" y2="1"><stop offset="0" stop-color="#b88a35"/><stop offset="1" stop-color="#e0c07a"/></linearGradient></defs>
      <path d="M0 0H248L124 56Z" fill="url(#goldFlap)"/>
    </svg>
    <div class="name">Kestrelmoor</div>
  </section>

  <section class="envelope env-blue">
    <svg width="248" height="78" viewBox="0 0 248 78" aria-hidden="true">
      <defs><linearGradient id="blueFlap" x1="0" y1="0" x2="0" y2="1"><stop offset="0" stop-color="#0d4f9e"/><stop offset="1" stop-color="#2a8ad8"/></linearGradient></defs>
      <path d="M0 0H248L124 56Z" fill="url(#blueFlap)"/>
    </svg>
    <div class="name">Kestrelmoor</div>
  </section>

  <section class="envelope env-white">
    <svg width="248" height="78" viewBox="0 0 248 78" aria-hidden="true">
      <path d="M0 0L124 56L248 0" fill="none" stroke="#d9dde3" stroke-width="1"/>
    </svg>
    <div class="name">Kestrelmoor</div>
  </section>

</div>
</body>
</html>
```